2024 Comprehensive Needs Assessment

Design our 2024 Binder Report Cover. Front, Spine, Back. We are in the Education field, reporting data for strategic planning. I have attached our color palette and the previous years covers as a sample.

```html
<!DOCTYPE html>
<html lang="en">
<head>
<meta charset="utf-8">
<title>2024 Comprehensive Needs Assessment – Cover</title>
<link href="https://fonts.googleapis.com/css2?family=Oswald:wght@400;500;700&display=swap" rel="stylesheet">
<style>
  :root {
    --page-bg: #eef1ee;
    --white: #ffffff;
    --navy: #1b2d63;
    --ink: #1a1a1a;
    --teal: #1fbaa8;
    --green: #3aae6e;
    --blue: #3a7fb8;
    --wood-light: #ead7bb;
    --wood-dark: #cfa77c;
    --leaf: #8cc63f;
  }
  html, body {
    margin: 0;
    width: 1200px;
    height: 1200px;
    overflow: hidden;
    background: var(--page-bg);
    font-family: "Oswald", "Arial Narrow", sans-serif;
  }
  .cover {
    position: absolute;
    left: 245px;
    top: 50px;
    width: 710px;
    height: 1100px;
    background: var(--white);
    overflow: hidden;
    box-shadow: 0 10px 30px rgba(0,0,0,0.12);
  }
  .cover-art {
    position: absolute;
    inset: 0;
    width: 710px;
    height: 1100px;
  }
  .title-block {
    position: absolute;
    left: 72px;
    top: 455px;
    color: var(--white);
  }
  .title-year {
    font-weight: 400;
    font-size: 50px;
    line-height: 1;
    letter-spacing: 1px;
  }
  .title-lead {
    margin-top: 18px;
    font-weight: 700;
    font-size: 76px;
    line-height: 1;
    letter-spacing: 0.5px;
  }
  .title-main {
    margin-top: -4px;
    margin-left: 6px;
    font-weight: 700;
    font-size: 222px;
    line-height: 0.92;
    color: var(--navy);
    letter-spacing: -1px;
  }
  .title-sub {
    margin-top: 0;
    margin-left: 6px;
    font-weight: 700;
    font-size: 108px;
    line-height: 0.95;
    color: var(--navy);
  }
  .district-name {
    margin-top: 4px;
    margin-left: 10px;
    font-weight: 500;
    font-size: 25px;
    color: var(--ink);
    letter-spacing: 0.3px;
  }
  .publisher {
    position: absolute;
    right: 40px;
    bottom: 40px;
    display: flex;
    align-items: center;
    gap: 10px;
  }
  .publisher-dot {
    width: 30px;
    height: 30px;
    border-radius: 50%;
    background: var(--leaf);
  }
  .publisher-name {
    font-weight: 400;
    font-size: 24px;
    color: var(--ink);
    line-height: 1.05;
  }
</style>
</head>
<body>
  <main class="cover">
    <svg class="cover-art" viewBox="0 0 710 1100" xmlns="http://www.w3.org/2000/svg">
      <defs>
        <linearGradient id="band-teal-green" x1="0" y1="0" x2="1" y2="0">
          <stop offset="0" stop-color="#1fbaa8"/>
          <stop offset="1" stop-color="#3aae6e"/>
        </linearGradient>
        <linearGradient id="band-blue" x1="0" y1="0" x2="1" y2="0">
          <stop offset="0" stop-color="#3a7fb8"/>
          <stop offset="1" stop-color="#1fb1b0"/>
        </linearGradient>
        <linearGradient id="photo-tone" x1="0" y1="0" x2="1" y2="1">
          <stop offset="0" stop-color="#ead7bb"/>
          <stop offset="0.6" stop-color="#dcbf98"/>
          <stop offset="1" stop-color="#cfa77c"/>
        </linearGradient>
      </defs>
      <!-- upper colour field -->
      <rect class="band-upper" x="0" y="0" width="710" height="820" fill="url(#band-teal-green)"/>
      <!-- right white sliver -->
      <path class="band-white-right" d="M710 480 C 650 560 600 600 560 620 L710 720 Z" fill="#ffffff"/>
      <!-- blue arc band -->
      <path class="band-blue" d="M0 560 C 120 470 300 450 470 470 C 560 480 640 510 700 560 L700 1100 L0 1100 Z" fill="url(#band-blue)"/>
      <!-- teal arc over blue -->
      <path class="band-teal" d="M120 620 C 260 560 480 560 710 640 L710 1100 L120 1100 Z" fill="#1fbaa8"/>
      <!-- white lower field -->
      <path class="field-white" d="M20 1100 C 30 900 200 730 460 730 C 580 730 660 760 710 790 L710 1100 Z" fill="#ffffff"/>
      <!-- photograph area -->
      <path class="cover-photo" role="img" aria-label="Photo: hands reviewing printed data charts beside a laptop on a wooden desk"
            d="M0 0 H665 C 700 200 560 420 300 432 C 170 438 60 400 0 360 Z" fill="url(#photo-tone)"/>
    </svg>

    <section class="title-block">
      <div class="title-year">2024</div>
      <div class="title-lead">COMPREHENSIVE</div>
      <div class="title-main">NEEDS</div>
      <div class="title-sub">ASSESSMENT</div>
      <div class="district-name">BRIARCREST SCHOOL DISTRICT</div>
    </section>

    <footer class="publisher">
      <span class="publisher-dot"></span>
      <span class="publisher-name">Brightpath<br>Learning, LLC</span>
    </footer>
  </main>
</body>
</html>
```